Bramblewick Keystone

Looking for modern business cards.
Clean contemporary design.
Similar to this.
https://www.snapvorlo.net/imgview?src=https%3A%2F%2Fcdn.printquell.net%2Fprofessional_elegant_modern_black_plain_metal_business_card-a1b2c3d4e5f60718293a4b5c6d7e8f90_qwxyz_4tmpl_540.jpg&ref=https%3A%2F%2Fwww.printquell.net%2Fprofessional_elegant_modern_black_plain_metal_business_card-100200300400500600&id=7aB9cD3e-QR5TU&tid=Xyz_abc123defGH%3A&v=10abcDEFghiJKLmnoPQRstUVwxYZ0123456789abcd..x&w=540&h=540&bih=1360&biw=1061&q=modern%20business%20cards&ref2=0abcDEFghiJKLmnoPQRstUVwxYZ0123456789abcd&ia=mrc&ua=8

But I'd like the blue to look metallic.

```html
<!DOCTYPE html>
<html lang="en">
<head>
<meta charset="utf-8">
<title>Bramblewick Keystone — Business Cards</title>
<link rel="stylesheet" href="https://fonts.googleapis.com/css2?family=Open+Sans:wght@600&family=Arimo:ital,wght@1,700&family=Roboto:wght@700&display=swap">
<style>
  :root {
    --page: #ffffff;
    --front-blue: #4aaebf;
    --front-blue-light: #5cc0cf;
    --front-blue-dark: #3e9fb3;
    --back-blue: #2e7f9f;
    --back-blue-light: #3a8fae;
    --back-blue-dark: #267592;
    --ink: #0b0b0b;
    --paper: #ffffff;
    --tagline: #1d3f6b;
    --email: #10202a;
  }
  * { margin: 0; padding: 0; box-sizing: border-box; }
  html, body {
    width: 1200px;
    height: 1200px;
    overflow: hidden;
    background: var(--page);
  }
  .canvas {
    position: relative;
    width: 1200px;
    height: 1200px;
  }
  .card {
    position: absolute;
    width: 870px;
    height: 510px;
    overflow: hidden;
  }
  .card-front {
    left: 101px;
    top: 149px;
    z-index: 2;
    background:
      repeating-linear-gradient(180deg, rgba(255,255,255,0.07) 0 1px, rgba(0,0,0,0) 1px 3px, rgba(0,0,0,0.04) 3px 4px),
      linear-gradient(165deg, rgba(255,255,255,0.22) 0%, rgba(255,255,255,0) 35%, rgba(255,255,255,0.14) 60%, rgba(0,0,0,0.06) 100%),
      linear-gradient(180deg, var(--front-blue-dark) 0%, var(--front-blue) 30%, var(--front-blue-light) 55%, var(--front-blue) 75%, var(--front-blue-light) 100%);
  }
  .card-back {
    left: 249px;
    top: 527px;
    z-index: 1;
    background:
      repeating-linear-gradient(180deg, rgba(255,255,255,0.05) 0 1px, rgba(0,0,0,0) 1px 3px, rgba(0,0,0,0.05) 3px 4px),
      linear-gradient(160deg, rgba(255,255,255,0.12) 0%, rgba(255,255,255,0) 40%, rgba(255,255,255,0.08) 65%, rgba(0,0,0,0.08) 100%),
      linear-gradient(180deg, var(--back-blue) 0%, var(--back-blue-light) 40%, var(--back-blue-dark) 100%);
  }
  .brand {
    position: absolute;
    left: 109px;
    top: 230px;
    display: flex;
    align-items: center;
    gap: 18px;
  }
  .brand-name {
    font-family: "Open Sans", sans-serif;
    font-weight: 600;
    font-size: 50px;
    line-height: 1;
    letter-spacing: -0.5px;
    white-space: nowrap;
  }
  .brand-dot {
    width: 22px;
    height: 22px;
    border-radius: 50%;
  }
  .card-front .brand-name { color: var(--ink); }
  .card-front .brand-dot { background: var(--ink); }
  .card-back .brand-name { color: var(--paper); }
  .card-back .brand-dot { background: var(--paper); }
  .tagline {
    position: absolute;
    left: 0;
    width: 910px;
    top: 302px;
    text-align: center;
    font-family: "Arimo", sans-serif;
    font-style: italic;
    font-weight: 700;
    font-size: 13px;
    letter-spacing: 2.4px;
    color: var(--tagline);
    white-space: nowrap;
  }
  .email {
    position: absolute;
    right: 258px;
    top: 300px;
    font-family: "Roboto", sans-serif;
    font-weight: 700;
    font-size: 14px;
    letter-spacing: 4.2px;
    color: var(--email);
    white-space: nowrap;
  }
</style>
</head>
<body>
  <main class="canvas">
    <section class="card card-back">
      <div class="brand">
        <span class="brand-name">Bramblewick Keystone</span>
        <span class="brand-dot"></span>
      </div>
      <p class="email">ada@bramblewick-keystone.com</p>
    </section>
    <section class="card card-front">
      <div class="brand">
        <span class="brand-name">Bramblewick Keystone</span>
        <span class="brand-dot"></span>
      </div>
      <p class="tagline">“Practical Leadership for Ambitious Teams”</p>
    </section>
  </main>
</body>
</html>
```